Bramble Roofing & Waterproofing HOA & Commercial Roofing Specialists

FRONT COVER (Panel 1)
Bramble Roofing & Waterproofing
HOA & Commercial Roofing Specialists
Protecting Communities.
Preserving Property Value.
Delivering Long-Term Solutions.
📍 Serving Orange County & Surrounding Areas
INSIDE LEFT PANEL (Panel 2)
Who We Are
Bramble Roofing & Waterproofing is a trusted HOA and commercial roofing specialist serving Orange County and surrounding areas. We understand the unique needs of homeowner associations, property managers, and commercial properties—delivering reliable service, clear communication, and long-lasting results.
✔ HOA-Focused Expertise
✔ Licensed & Insured
✔ Emergency Response Available
✔ Quality Workmanship You Can Trust
INSIDE MIDDLE PANEL (Panel 3)
Roofing Services
HOA & Commercial Roofing
• Emergency roof tarping & repairs — Starting at $550
• Small & large roof repairs
• Chimney cap and spark arrestor repairs
• Preventative roof maintenance
• Roof cleaning
• Full roof replacement
We work on all roof types:
✔ Flat Roofs (Torch down, TPO, & PVC)
✔ Tile Roofs (Clay tiles, concrete tiles, and more)
✔ Shingle Roofs - KTV certified contractor
• Coating (silicone or acrylic)
No matter the size or system—we’ve got you covered.
INSIDE RIGHT PANEL (Panel 4)
Gutter Services
• Small & large gutter repairs
• Gutter cleaning & maintenance
• New gutter installation & replacement
Proper drainage protects your building—let us handle it.
BACK LEFT PANEL (Panel 5)
Deck/Balcony Waterproofing Services
• Balcony/deck maintenance
• Deck resurfacing
• Small & large deck repairs
• Full deck reconstruction
Specialized waterproofing solutions to keep decks safe, compliant, and durable.
BACK COVER (Panel 6)
Why Choose Bramble?
✔ HOA & Commercial Specialists
✔ Fully Licensed & Insured
✔ Reliable Scheduling
✔ Clear Communication
✔ Quality Materials & Craftsmanship
License Information:
C-39 Roofing Contractor
General B Contractor
License #5372941
📍 Office Location:
41 Tolliver Street, Suite D Irvine, CA 92604
📞 Contact us today for a consultation
949-555-0162 or rfp@bramblecrest.example
🌐 Serving Orange County & surrounding areas
- Gotham

```html
<!DOCTYPE html>
<html lang="en">
<head>
<meta charset="utf-8">
<title>Bramble Roofing &amp; Waterproofing – Trifold Brochure</title>
<link rel="stylesheet" href="https://fonts.googleapis.com/css2?family=Montserrat:wght@400;500;600;700;800&family=Lora:ital,wght@1,700&display=swap">
<style>
:root{
  --stage:#868686;
  --paper:#f3f4f6;
  --ink:#111214;
  --black:#0a0a0b;
  --blue:#1ba4ea;
  --blue-deep:#0b78c9;
  --white:#ffffff;
  --grey-text:#3b3d42;
}
*{box-sizing:border-box;margin:0;padding:0}
html,body{width:1162px;height:1200px;overflow:hidden}
body{background:var(--stage);font-family:"Montserrat",Arial,sans-serif;color:var(--ink);position:relative}

.stage-label{position:absolute;top:34px;font-weight:800;font-size:25px;letter-spacing:9px;color:var(--white)}
.label-outside{left:372px}
.label-front{left:906px}
.label-inside{left:388px;top:606px}
.label-back{left:906px;top:606px}

.spread{position:absolute;overflow:hidden;background:var(--paper)}
.outside{left:76px;top:76px;width:722px;height:511px}
.inside{left:76px;top:644px;width:727px;height:514px}
.panel{position:absolute;top:0;height:100%;overflow:hidden}
.panel > svg.bg{position:absolute;inset:0;width:100%;height:100%}
.standalone{position:absolute;background:var(--paper);overflow:hidden}
.front{left:833px;top:76px;width:245px;height:511px}
.back{left:833px;top:644px;width:243px;height:514px}

/* wordmark */
.wordmark{position:absolute;left:0;right:0;text-align:center}
.wordmark .name{display:inline-flex;align-items:center;gap:5px;font-weight:800;font-size:23px;letter-spacing:.5px;line-height:1}
.wordmark .name::after{content:"";width:7px;height:7px;border-radius:50%;background:currentColor}
.wordmark .tag{display:block;font-weight:500;font-size:7.6px;letter-spacing:.6px;margin-top:7px}
.wordmark.light .name,.wordmark.light .tag{color:var(--white)}
.wordmark.dark .name,.wordmark.dark .tag{color:var(--ink)}

/* pills */
.title-pill{position:absolute;background:linear-gradient(180deg,#2c2d30,#050506);color:var(--white);font-weight:800;border-radius:30px;display:flex;align-items:center}
.title-pill .accent{color:var(--blue)}

.badge{position:absolute;width:133px;height:55px;border-radius:28px;background:linear-gradient(180deg,#303134,#020203);border:2px solid var(--white);box-shadow:0 2px 5px rgba(0,0,0,.35);display:flex;align-items:center;padding-left:52px;color:var(--white);font-size:8.3px;font-weight:500;line-height:10.5px}
.badge .icon{position:absolute;left:6px;top:50%;width:40px;height:40px;margin-top:-20px;border-radius:50%;background:var(--blue);border:2px solid #bfe8fc;display:flex;align-items:center;justify-content:center}
.badge .icon svg{width:22px;height:22px}
.badge.small{width:131px;height:53px}

/* ticks */
.ticks{list-style:none;font-size:7.3px;line-height:10.2px;color:var(--grey-text)}
.ticks li{position:relative;padding-left:10px}
.ticks li::before{content:"";position:absolute;left:0;top:2px;width:6px;height:6px;border:1px solid var(--blue);border-radius:50%}
.ticks li::after{content:"";position:absolute;left:2.6px;top:3.6px;width:1.6px;height:3px;border:solid var(--blue);border-width:0 1px 1px 0;transform:rotate(45deg)}
.ticks.inline{display:flex;gap:10px}

.photo{position:absolute;border-radius:14px}

/* deck panel */
.deck-title{left:24px;top:39px;width:193px;height:54px;justify-content:center;text-align:center;font-size:15px;line-height:18px}
.deck-photo{left:23px;top:105px;width:196px;height:151px;background:linear-gradient(135deg,#8a8f86 0%,#5a4431 40%,#7b5535 70%,#3f3328 100%)}
.drops{position:absolute;left:36px;top:268px;list-style:none;font-size:10.6px;line-height:15.5px;color:#1e1f22}
.drops li{position:relative;padding-left:13px}
.drops li::before{content:"";position:absolute;left:1px;top:4px;width:6px;height:6px;background:var(--blue);border-radius:0 50% 50% 50%;transform:rotate(45deg)}
.deck-claim{position:absolute;left:0;right:0;top:425px;text-align:center;color:var(--white);font-weight:700;font-size:12.6px;line-height:17px}
.deck-points{position:absolute;left:0;right:0;top:471px;display:flex;justify-content:center;gap:6px;color:var(--blue);font-size:8.6px;font-weight:500}
.deck-points span{display:flex;align-items:center;gap:3px}
.deck-points span::before{content:"✓";width:10px;height:10px;border-radius:50%;background:var(--white);color:var(--black);font-size:7px;font-weight:800;display:flex;align-items:center;justify-content:center}

/* info panel */
.info .wordmark{top:22px}
.why-title{position:absolute;left:0;right:0;top:110px;text-align:center;font-weight:800;font-size:16.4px;color:var(--ink)}
.why-title .accent{color:var(--blue)}
.why-cols{position:absolute;left:24px;top:139px;display:flex;gap:4px}
.why-cols .ticks:first-child{width:110px}
.why-cols .ticks:last-child{width:102px}
.license{position:absolute;left:0;right:0;top:196px;text-align:center}
.license h3{font-size:11.6px;font-weight:700;margin-bottom:4px}
.license p{font-size:7.8px;line-height:10.4px;color:var(--grey-text)}
.contact-box{position:absolute;left:25px;top:349px;width:190px;height:80px;border:1.2px solid var(--white);border-radius:8px;text-align:center;color:var(--white)}
.contact-box .phone-ring{position:absolute;left:50%;top:-16px;margin-left:-15px;width:30px;height:30px;border-radius:50%;background:var(--black);border:1.6px solid var(--white);display:flex;align-items:center;justify-content:center}
.contact-box .phone-ring svg{width:15px;height:15px}
.contact-box .line1{margin-top:15px;font-size:13px;font-weight:700;line-height:15px}
.contact-box .line2{font-size:16px;font-weight:700;line-height:20px}
.contact-box .tel{font-size:11.6px;line-height:16px;margin-top:2px}
.contact-box .mail{position:absolute;left:50%;bottom:-8px;transform:translateX(-50%);white-space:nowrap;background:var(--black);padding:0 4px;font-size:10px;line-height:14px}
.address{position:absolute;left:0;right:0;top:449px;text-align:center;color:var(--white);font-size:9.6px}
.area-pill{position:absolute;left:16px;width:210px;top:471px;height:17px;border-radius:9px;background:var(--blue-deep);color:var(--white);font-size:8.6px;font-weight:500;display:flex;align-items:center;justify-content:center;gap:4px}
.area-pill svg{width:9px;height:10px}

/* cover */
.cover .wordmark{top:26px;left:0;right:auto;width:177px}
.cover-title{position:absolute;left:0;right:0;top:389px;text-align:center;font-weight:800;font-size:19.6px;line-height:26px;color:var(--white)}
.cover-title .accent{color:var(--blue)}
.cover-sub{position:absolute;left:0;right:0;top:445px;text-align:center;color:var(--white);font-size:10.8px;font-weight:500}
.cover .area-pill{left:19px;width:210px}

/* inside */
.who-title{left:24px;top:22px;width:179px;height:34px;padding-left:15px;font-size:17.5px}
.who-copy{position:absolute;left:27px;top:66px;width:197px;font-size:7.9px;line-height:10.4px;color:var(--white)}
.service-title{top:22px;width:179px;height:34px;padding-left:16px;font-size:17.5px}
.roof-photo{left:263px;top:66px;width:208px;height:242px;background:linear-gradient(160deg,#b8c6d8 0%,#8d939c 35%,#4b4f57 70%,#2e3137 100%)}
.gutter-photo{left:504px;top:66px;width:209px;height:242px;background:linear-gradient(170deg,#aeb7bd 0%,#7d8578 40%,#5a5f5e 70%,#c9c7c0 100%)}
.block-title{position:absolute;font-weight:800;font-size:13px;color:var(--ink)}
.roof-ticks{position:absolute;left:266px;top:341px;display:flex;gap:6px}
.roof-ticks .ticks:first-child{width:82px}
.roof-ticks strong{color:var(--ink);font-weight:700;white-space:nowrap}
.roof-types{position:absolute;left:266px;top:404px}
.gutter-ticks{position:absolute;left:521px;top:322px}
.drain-line{position:absolute;left:486px;width:241px;top:362px;text-align:center;font-family:"Lora",Georgia,serif;font-style:italic;font-weight:700;font-size:13px;line-height:16px;color:var(--blue-deep)}
.inside .wordmark.dark{left:486px;right:auto;width:241px;top:410px}
.cover-line{position:absolute;left:245px;width:241px;top:471px;text-align:center;font-family:"Lora",Georgia,serif;font-style:italic;font-weight:700;font-size:13px;line-height:16px;color:var(--white)}
</style>
</head>
<body>

<div class="stage-label label-outside">OUTSIDE</div>
<div class="stage-label label-front">FRONT</div>
<div class="stage-label label-inside">INSIDE</div>
<div class="stage-label label-back">BACK</div>

<!-- ===== Outside spread ===== -->
<div class="spread outside">

  <section class="panel deck" style="left:0;width:236px">
    <svg class="bg" viewBox="0 0 236 511" preserveAspectRatio="none" aria-hidden="true">
      <rect width="236" height="511" fill="var(--paper)"/>
      <path d="M60 0 C130 6 200 24 236 44 L236 52 C196 32 126 10 60 3Z" fill="var(--blue)"/>
      <path d="M0 380 C80 376 170 346 236 296 L236 312 C170 365 80 395 0 400Z" fill="var(--blue)"/>
      <path d="M0 400 C80 395 170 365 236 312 V511 H0Z" fill="var(--black)"/>
    </svg>
    <div class="title-pill deck-title">Deck &amp;<br>Balcony Services</div>
    <div class="photo deck-photo" role="img" aria-label="Photo of a worker repairing weathered wooden deck steps"></div>
    <ul class="drops">
      <li>Balcony &amp; deck maintenance</li>
      <li>Deck resurfacing</li>
      <li>Small &amp; large deck repairs</li>
      <li>Full deck reconstruction</li>
    </ul>
    <p class="deck-claim">Specialized waterproofing<br>solutions to keep</p>
    <div class="deck-points"><span>Decks safe</span><span>Compliant</span><span>Durable</span></div>
  </section>

  <section class="panel info" style="left:236px;width:241px">
    <svg class="bg" viewBox="0 0 241 511" preserveAspectRatio="none" aria-hidden="true">
      <rect width="241" height="511" fill="var(--paper)"/>
      <path d="M0 44 C40 62 70 84 120 86 C170 84 205 50 241 0 H0Z" fill="var(--blue-deep)" opacity=".5"/>
      <path d="M0 44 C40 60 70 80 120 80 C170 78 205 40 241 0 H0Z" fill="var(--blue)"/>
      <path d="M55 274 C105 258 160 260 205 276" fill="none" stroke="var(--blue)" stroke-width="4" stroke-linecap="round" opacity=".85"/>
      <path d="M0 312 C60 285 170 268 241 316 V511 H0Z" fill="var(--black)"/>
    </svg>
    <div class="wordmark light"><span class="name">BRAMBLE</span><span class="tag">ROOFING &amp; WATERPROOFING</span></div>
    <h2 class="why-title">Why Choose <span class="accent">Bramble?</span></h2>
    <div class="why-cols">
      <ul class="ticks"><li>HOA &amp; Commercial<br>Specialists</li><li>Fully Licensed &amp; Insured</li><li>Reliable Scheduling</li></ul>
      <ul class="ticks"><li>Clear Communication</li><li>Quality Materials &amp;<br>Craftsmanship</li></ul>
    </div>
    <div class="license"><h3>License Information</h3><p>C-39 Roofing Contractor<br>General B Contractor<br>License #5372941</p></div>
    <div class="contact-box">
      <span class="phone-ring"><svg viewBox="0 0 24 24"><path d="M6.6 10.8a15 15 0 0 0 6.6 6.6l2.2-2.2a1 1 0 0 1 1-.25 11 11 0 0 0 3.6.6 1 1 0 0 1 1 1V20a1 1 0 0 1-1 1A17 17 0 0 1 3 4a1 1 0 0 1 1-1h3.5a1 1 0 0 1 1 1 11 11 0 0 0 .6 3.6 1 1 0 0 1-.25 1Z" fill="#fff"/></svg></span>
      <p class="line1">Contact us today</p>
      <p class="line2">for a consultation</p>
      <p class="tel">949-555-0162</p>
      <p class="mail">or rfp@bramblecrest.example</p>
    </div>
    <p class="address">41 Tolliver Street, Suite D Irvine, CA 92604</p>
    <div class="area-pill"><svg viewBox="0 0 10 12"><path d="M5 0a4 4 0 0 0-4 4c0 3 4 8 4 8s4-5 4-8a4 4 0 0 0-4-4Zm0 5.6A1.6 1.6 0 1 1 5 2.4a1.6 1.6 0 0 1 0 3.2Z" fill="#fff"/></svg>Serving Orange County &amp; Surrounding Areas</div>
  </section>

  <section class="panel cover" style="left:477px;width:245px">
    <svg class="bg" viewBox="0 0 245 511" preserveAspectRatio="none" aria-hidden="true">
      <defs><linearGradient id="roofer-a" x1="0" y1="0" x2="1" y2="1"><stop offset="0" stop-color="#c9d3dc"/><stop offset=".45" stop-color="#5d7890"/><stop offset="1" stop-color="#1f4f86"/></linearGradient></defs>
      <rect width="245" height="511" fill="var(--paper)"/>
      <path d="M0 0 H92 C60 8 25 24 0 40Z" fill="var(--blue)"/>
      <g role="img" aria-label="Photo of a roofer in a hard hat working on a standing-seam metal roof"><path d="M198 15 L245 105 V360 C215 372 190 374 170 372 C105 366 72 300 100 232Z" fill="url(#roofer-a)"/></g>
      <path d="M110 352 C150 378 205 382 245 362" fill="none" stroke="var(--blue)" stroke-width="6"/>
      <path d="M0 316 C80 330 150 385 245 372 V511 H0Z" fill="var(--black)"/>
    </svg>
    <div class="wordmark dark"><span class="name">BRAMBLE</span><span class="tag">ROOFING &amp; WATERPROOFING</span></div>
    <div class="badge" style="left:38px;top:145px"><span class="icon"><svg viewBox="0 0 24 24" fill="none" stroke="#fff" stroke-width="1.6"><path d="M12 2 4 5v6c0 5 3.5 9 8 11 4.5-2 8-6 8-11V5Z"/><circle cx="12" cy="10" r="2.2"/><path d="M8.5 16a3.5 3.5 0 0 1 7 0"/></svg></span>Protecting<br>Communities</div>
    <div class="badge" style="left:13px;top:206px"><span class="icon"><svg viewBox="0 0 24 24" fill="none" stroke="#fff" stroke-width="1.6"><circle cx="12" cy="12" r="3.5"/><path d="M12 4v3M12 17v3M4 12h3M17 12h3M6.3 6.3l2.1 2.1M15.6 15.6l2.1 2.1M6.3 17.7l2.1-2.1M15.6 8.4l2.1-2.1"/></svg></span>Delivering<br>Long-Term<br>Solutions.</div>
    <div class="badge" style="left:38px;top:266px"><span class="icon"><svg viewBox="0 0 24 24" fill="none" stroke="#fff" stroke-width="1.6"><path d="M3 11 12 3l9 8M5 9.5V21h14V9.5"/><path d="M9 18v-3M12 18v-5M15 18v-4"/></svg></span>Preserving<br>Property Value</div>
    <h1 class="cover-title">Bramble Roofing &amp;<br><span class="accent">Waterproofing</span></h1>
    <p class="cover-sub">HOA &amp; Commercial Roofing Specialists</p>
    <div class="area-pill"><svg viewBox="0 0 10 12"><path d="M5 0a4 4 0 0 0-4 4c0 3 4 8 4 8s4-5 4-8a4 4 0 0 0-4-4Zm0 5.6A1.6 1.6 0 1 1 5 2.4a1.6 1.6 0 0 1 0 3.2Z" fill="#fff"/></svg>Serving Orange County &amp; Surrounding Areas</div>
  </section>
</div>

<!-- ===== Front cover ===== -->
<section class="standalone front cover">
  <svg style="position:absolute;inset:0;width:100%;height:100%" viewBox="0 0 245 511" preserveAspectRatio="none" aria-hidden="true">
    <defs><linearGradient id="roofer-b" x1="0" y1="0" x2="1" y2="1"><stop offset="0" stop-color="#c9d3dc"/><stop offset=".45" stop-color="#5d7890"/><stop offset="1" stop-color="#1f4f86"/></linearGradient></defs>
    <rect width="245" height="511" fill="var(--paper)"/>
    <path d="M0 0 H92 C60 8 25 24 0 40Z" fill="var(--blue)"/>
    <g role="img" aria-label="Photo of a roofer in a hard hat working on a standing-seam metal roof"><path d="M198 15 L245 105 V360 C215 372 190 374 170 372 C105 366 72 300 100 232Z" fill="url(#roofer-b)"/></g>
    <path d="M110 352 C150 378 205 382 245 362" fill="none" stroke="var(--blue)" stroke-width="6"/>
    <path d="M0 316 C80 330 150 385 245 372 V511 H0Z" fill="var(--black)"/>
  </svg>
  <div class="wordmark dark"><span class="name">BRAMBLE</span><span class="tag">ROOFING &amp; WATERPROOFING</span></div>
  <div class="badge" style="left:38px;top:145px"><span class="icon"><svg viewBox="0 0 24 24" fill="none" stroke="#fff" stroke-width="1.6"><path d="M12 2 4 5v6c0 5 3.5 9 8 11 4.5-2 8-6 8-11V5Z"/><circle cx="12" cy="10" r="2.2"/><path d="M8.5 16a3.5 3.5 0 0 1 7 0"/></svg></span>Protecting<br>Communities</div>
  <div class="badge" style="left:13px;top:206px"><span class="icon"><svg viewBox="0 0 24 24" fill="none" stroke="#fff" stroke-width="1.6"><circle cx="12" cy="12" r="3.5"/><path d="M12 4v3M12 17v3M4 12h3M17 12h3M6.3 6.3l2.1 2.1M15.6 15.6l2.1 2.1M6.3 17.7l2.1-2.1M15.6 8.4l2.1-2.1"/></svg></span>Delivering<br>Long-Term<br>Solutions.</div>
  <div class="badge" style="left:38px;top:266px"><span class="icon"><svg viewBox="0 0 24 24" fill="none" stroke="#fff" stroke-width="1.6"><path d="M3 11 12 3l9 8M5 9.5V21h14V9.5"/><path d="M9 18v-3M12 18v-5M15 18v-4"/></svg></span>Preserving<br>Property Value</div>
  <h1 class="cover-title">Bramble Roofing &amp;<br><span class="accent">Waterproofing</span></h1>
  <p class="cover-sub">HOA &amp; Commercial Roofing Specialists</p>
  <div class="area-pill"><svg viewBox="0 0 10 12"><path d="M5 0a4 4 0 0 0-4 4c0 3 4 8 4 8s4-5 4-8a4 4 0 0 0-4-4Zm0 5.6A1.6 1.6 0 1 1 5 2.4a1.6 1.6 0 0 1 0 3.2Z" fill="#fff"/></svg>Serving Orange County &amp; Surrounding Areas</div>
</section>

<!-- ===== Inside spread ===== -->
<div class="spread inside">
  <svg style="position:absolute;inset:0;width:100%;height:100%" viewBox="0 0 727 514" preserveAspectRatio="none" aria-hidden="true">
    <defs>
      <linearGradient id="who-bg" x1="0" y1="0" x2="0" y2="1"><stop offset="0" stop-color="#1ba4ea"/><stop offset="1" stop-color="#3bb6f2"/></linearGradient>
      <linearGradient id="crew" x1="0" y1="0" x2="1" y2="1"><stop offset="0" stop-color="#9fb4cc"/><stop offset=".45" stop-color="#3d4a5a"/><stop offset=".8" stop-color="#8a5a3a"/><stop offset="1" stop-color="#b0342f"/></linearGradient>
    </defs>
    <rect width="727" height="514" fill="var(--paper)"/>
    <rect width="245" height="514" fill="url(#who-bg)"/>
    <g role="img" aria-label="Photo of two roofers in hard hats inspecting a metal roof from a scaffold"><path d="M48 152 L0 232 V514 H160 C140 460 118 380 110 300Z" fill="url(#crew)" stroke="#fff" stroke-width="3"/></g>
    <path d="M150 514 C220 486 300 456 420 450 C560 444 650 448 727 452 V466 C650 460 560 456 420 460 C320 466 250 492 205 514Z" fill="var(--blue)"/>
    <path d="M175 514 C235 488 310 460 420 456 C560 452 650 458 727 466 V514Z" fill="var(--black)"/>
  </svg>

  <div class="title-pill who-title">Who&nbsp;<span class="accent">We Are</span></div>
  <p class="who-copy">Bramble Roofing &amp; Waterproofing is a trusted HOA and commercial roofing specialist serving Orange County and surrounding areas. We understand the unique needs of homeowner associations, property managers, and commercial properties—delivering reliable service, clear communication, and long-lasting results.</p>
  <div class="badge small" style="left:57px;top:210px"><span class="icon"><svg viewBox="0 0 24 24" fill="none" stroke="#fff" stroke-width="1.6"><circle cx="10" cy="11" r="3"/><path d="M10 4v2M10 16v2M3 11h2M15 11h2"/><circle cx="17" cy="17" r="3.5"/><path d="m15.5 17 1.2 1.2 2-2.2"/></svg></span>HOA-Focused<br>Expertise</div>
  <div class="badge small" style="left:88px;top:271px"><span class="icon"><svg viewBox="0 0 24 24" fill="none" stroke="#fff" stroke-width="1.6"><rect x="4" y="3" width="12" height="17" rx="1"/><path d="M7 7h6M7 10h6M7 13h3"/><circle cx="17" cy="15" r="3"/><path d="M16 18v3l1-1 1 1v-3"/></svg></span>Licensed &amp;<br>Insured</div>
  <div class="badge small" style="left:102px;top:334px"><span class="icon"><svg viewBox="0 0 24 24" fill="none" stroke="#fff" stroke-width="1.6"><path d="M6 4h3l1.5 4-2 1.2a9 9 0 0 0 4.3 4.3L14 11.5l4 1.5v3a2 2 0 0 1-2 2A13 13 0 0 1 4 6a2 2 0 0 1 2-2Z"/><circle cx="17" cy="7" r="3.5"/><path d="M17 5.5v3M15.5 7h3"/></svg></span>Emergency<br>Response<br>Available</div>
  <div class="badge small" style="left:102px;top:397px"><span class="icon"><svg viewBox="0 0 24 24" fill="none" stroke="#fff" stroke-width="1.6"><path d="M2 11 6 7l4 2 3-2 5 3 4-3"/><path d="m6 7 5 9a1.5 1.5 0 0 0 2.4.2L18 11"/><path d="M10 14l2 2M12 12l2 2"/></svg></span>Emergency<br>Response<br>Available</div>

  <div class="title-pill service-title" style="left:263px">Roofing&nbsp;<span class="accent">Services</span></div>
  <div class="photo roof-photo" role="img" aria-label="Photo of a roofer nailing new asphalt shingles over underlayment"></div>
  <h3 class="block-title" style="left:266px;top:317px">HOA &amp; Commercial Roofing</h3>
  <div class="roof-ticks">
    <ul class="ticks"><li>Emergency roof<br>tarping &amp; repairs<br><strong>Starting at $550</strong></li></ul>
    <ul class="ticks"><li>Small &amp; large roof repairs</li><li>Preventative roof maintenance</li><li>Full roof replacement</li></ul>
  </div>
  <h3 class="block-title" style="left:266px;top:381px">We work on all roof types</h3>
  <ul class="ticks inline roof-types"><li>Flat Roofs</li><li>Tile Roofs</li><li>Shingle Roofs</li></ul>

  <div class="title-pill service-title" style="left:506px">Gutter&nbsp;<span class="accent">Services</span></div>
  <div class="photo gutter-photo" role="img" aria-label="Photo of a pressure washer cleaning a roof gutter"></div>
  <ul class="ticks gutter-ticks"><li>Small &amp; large gutter repairs</li><li>Gutter cleaning &amp; maintenance</li><li>New gutter installation &amp; replacement</li></ul>
  <p class="drain-line">Proper drainage protects your<br>building—let us handle it.</p>
  <div class="wordmark dark"><span class="name">BRAMBLE</span><span class="tag">ROOFING &amp; WATERPROOFING</span></div>

  <p class="cover-line">No matter the size or system<br>—we’ve got you covered.</p>
</div>

<!-- ===== Back cover ===== -->
<section class="standalone back info">
  <svg style="position:absolute;inset:0;width:100%;height:100%" viewBox="0 0 243 514" preserveAspectRatio="none" aria-hidden="true">
    <rect width="243" height="514" fill="var(--paper)"/>
    <path d="M0 0 H243 V48 C205 70 170 86 121 86 C72 86 38 70 0 48Z" fill="var(--blue-deep)" opacity=".5"/>
    <path d="M0 0 H243 V42 C205 64 170 80 121 80 C72 80 38 64 0 42Z" fill="var(--blue)"/>
    <path d="M55 278 C105 262 160 264 205 280" fill="none" stroke="var(--blue)" stroke-width="4" stroke-linecap="round" opacity=".85"/>
    <path d="M0 302 C60 280 170 266 243 317 V514 H0Z" fill="var(--black)"/>
  </svg>
  <div class="wordmark light"><span class="name">BRAMBLE</span><span class="tag">ROOFING &amp; WATERPROOFING</span></div>
  <h2 class="why-title">Why Choose <span class="accent">Bramble?</span></h2>
  <div class="why-cols" style="top:141px">
    <ul class="ticks"><li>HOA &amp; Commercial<br>Specialists</li><li>Fully Licensed &amp; Insured</li><li>Reliable Scheduling</li></ul>
    <ul class="ticks"><li>Clear Communication</li><li>Quality Materials &amp;<br>Craftsmanship</li></ul>
  </div>
  <div class="license" style="top:198px"><h3>License Information</h3><p>C-39 Roofing Contractor<br>General B Contractor<br>License #5372941</p></div>
  <div class="contact-box" style="left:24px;top:351px;width:192px">
    <span class="phone-ring"><svg viewBox="0 0 24 24"><path d="M6.6 10.8a15 15 0 0 0 6.6 6.6l2.2-2.2a1 1 0 0 1 1-.25 11 11 0 0 0 3.6.6 1 1 0 0 1 1 1V20a1 1 0 0 1-1 1A17 17 0 0 1 3 4a1 1 0 0 1 1-1h3.5a1 1 0 0 1 1 1 11 11 0 0 0 .6 3.6 1 1 0 0 1-.25 1Z" fill="#fff"/></svg></span>
    <p class="line1">Contact us today</p>
    <p class="line2">for a consultation</p>
    <p class="tel">949-555-0162</p>
    <p class="mail">or rfp@bramblecrest.example</p>
  </div>
  <p class="address" style="top:454px">41 Tolliver Street, Suite D Irvine, CA 92604</p>
  <div class="area-pill" style="left:15px;width:211px;top:476px"><svg viewBox="0 0 10 12"><path d="M5 0a4 4 0 0 0-4 4c0 3 4 8 4 8s4-5 4-8a4 4 0 0 0-4-4Zm0 5.6A1.6 1.6 0 1 1 5 2.4a1.6 1.6 0 0 1 0 3.2Z" fill="#fff"/></svg>Serving Orange County &amp; Surrounding Areas</div>
</section>

</body>
</html>
```